Label Design for RTD Cocktail Line Tovelin Spirits

Tovelin Spirits is a line of Indian-inspired artisan cocktails that "brings the bartender home" for professional men and women who like the finer things in life but don’t always have the time to treat themselves. No need for a multitude of expensive and hard-to-find ingredients, time consuming recipes, or a mixologist.

Our line of 3 open and serve cocktails blends a range of premium spirits with exotic ingredients so you can conveniently raise a glass for any of life’s celebrations.

Our bottle is the 750ml Claret bottle with Quarnet (screw cap) closure and will be covered entirely in a shrink sleeve (so potentially anything can be designed for any part of the bottle). We want the bottle to pop on the shelf so it should look different than what’s already out there (Velvet Moth, Galdrova, Merlusa ready to drink cocktails). We are looking for a sexy design that's polished/sleek.
Updates

Project Deadline Extended
Reason: Hello designers! Tovelin Spirits is so impressed with what we have received thus far and we would like to give some of the designers a few extra days to make the edits we requested. It's never too late to submit! Thank you all!

Industry/Entity Type

It Professional

Requirements
Must have
• Front of bottle
* “Tovelin Spirits” name and Peacock Logo- but feel free to pull the elements apart and use them on the bottle in different ways
* Open & Serve
* 12% ALC/VOL
* 750 ml
* 3 different labels in a theme for
-Borvelle
-Faluntera
-Pomadrine

Borvelle Ideas- soft brown palate, the ingredients in chai spice (cloves, cardamom pods, nutmeg, black peppercorns, star anise, and cinnamon stick)

Faluntera Ideas -cool and refreshing, pale green shade (not clashing with logo), graphics of fresh mint leaves, green chili, lime, cucumber

Pomadrine Ideas- soft/pale pink shades, graphics of lychi fruit (outer red shell and inner pink flesh), ginger

Back of bottle
* explanation of the 3 cocktails
Borvelle: Forget what you think you know about chai, this is not the Queen’s tea-time drink! Borvelle is a smooth, sweetly -spiced cocktail made with vodka, black tea, and a combination of aromatic spices. This velvety cocktail is rich without being heavy. Enjoy chilled or over ice anytime.

Faluntera: Faluntera can’t make up its mind! This fusion of zesty lime, sweet mint, earthy cucumber and spicy chilies is so refreshing you’ll crave it on a hot summer day or a cool winter’s night. The exotic botanicals in gin add a complexity to the cocktail making this a refreshing but potent drink! Enjoy chilled or over ice anytime.

Pomadrine: East meet West. Delicate lychi meet hard-hitting whiskey. Pomadrine will tempt you senses with flavor, fragrance and beauty. The peppery kick of ginger and the intensity of the un-aged whiskey are softened by lychi’s intoxicating scent and subtle, sweet finish.

Please include
1. Bottled By QRW Spirits Company
2. Sample barcode (where you would place it in your design)
3. www.TovelinSpirits.example
4. GOVERNMENT WARNING: (1) According to the Surgeon General, women should not drink alcoholic beverages during pregnancy because of the risk of birth defects. (2) Consumption of alcoholic beverages impairs your ability to drive a car or operate machinery, and may cause health problems.

Optional to include
*"Bring the Bartender Home"
*"Tovelin Spirits” name and Peacock Logo on the back
*Entirely black sleeve with contrasting design

FYI the Fonts used in our logo are Geosans Light and Prakrta, but feel free to use other complimentary fonts on the other aspects.
Nice to have
• Optional to include

```html
<!DOCTYPE html>
<html lang="en">
<head>
<meta charset="utf-8">
<title>Tovelin Spirits — RTD Cocktail Labels</title>
<link href="https://fonts.googleapis.com/css2?family=Kaushan+Script&family=Dancing+Script:wght@400&family=Oswald:wght@600&family=Questrial&display=swap" rel="stylesheet">
<style>
  :root {
    --bg: #ffffff;
    --cap: #111111;
    --logo-grey: #4a4a4c;
    --faluntera: #1f5d30;
    --faluntera-soft: #86ad6b;
    --borvelle: #5a3414;
    --borvelle-soft: #8c6a4d;
    --pomadrine: #8d1421;
    --pomadrine-soft: #d7868f;
  }
  * { box-sizing: border-box; margin: 0; padding: 0; }
  html, body { width: 1200px; height: 844px; overflow: hidden; background: var(--bg); }
  .canvas { position: relative; width: 1200px; height: 844px; }

  .bottle { position: absolute; top: 62px; width: 200px; height: 780px; }
  .bottle--faluntera { left: 109px; --tone: var(--faluntera); --tone-soft: var(--faluntera-soft); }
  .bottle--borvelle { left: 508px; --tone: var(--borvelle); --tone-soft: var(--borvelle-soft); }
  .bottle--pomadrine { left: 906px; --tone: var(--pomadrine); --tone-soft: var(--pomadrine-soft); }

  .bottle__shape { position: absolute; inset: 0; width: 200px; height: 780px; }

  .neck-band {
    position: absolute; top: 88px; left: 61px; width: 78px; height: 48px;
    background: var(--tone);
    display: flex; align-items: center; justify-content: center;
  }
  .neck-band::after {
    content: ""; position: absolute; inset: 0;
    background: linear-gradient(90deg, rgba(0,0,0,0.28) 0%, rgba(255,255,255,0.12) 35%, rgba(255,255,255,0) 60%, rgba(0,0,0,0.3) 100%);
  }
  .neck-band__text {
    position: relative; z-index: 1;
    font-family: "Oswald", sans-serif; font-weight: 600; font-size: 14px;
    color: #fff; white-space: nowrap; letter-spacing: 0;
  }

  .flavour-splash {
    position: absolute; top: 272px; left: 26px; width: 148px; height: 92px;
    border-radius: 50%;
    background: radial-gradient(ellipse at 50% 55%, var(--tone) 0%, var(--tone-soft) 40%, rgba(255,255,255,0) 70%);
    opacity: 0.7;
  }

  .flavour-name {
    position: absolute; top: 366px; left: 0; width: 200px; text-align: center;
    font-family: "Kaushan Script", cursive; font-weight: 400; font-size: 34px; line-height: 1;
    color: var(--tone); white-space: nowrap;
  }
  .flavour-name__accent { font-size: 40px; }

  .ingredients {
    position: absolute; top: 446px; left: 10px; width: 180px; text-align: center;
    font-family: "Dancing Script", cursive; font-size: 12px; line-height: 1.3;
    color: var(--tone);
  }

  .brand { position: absolute; top: 540px; left: 0; width: 200px; text-align: center; }
  .brand__mark {
    display: block; width: 36px; height: 36px; margin: 0 auto 12px;
    border-radius: 50%; background: var(--logo-grey);
  }
  .brand__name {
    font-family: "Questrial", sans-serif; font-size: 18px; color: var(--logo-grey);
    white-space: nowrap;
  }

  .spec {
    position: absolute; top: 672px; font-family: "Questrial", sans-serif;
    font-size: 10px; color: var(--tone);
  }
  .spec--abv { left: 30px; }
  .spec--volume { right: 30px; }
</style>
</head>
<body>
<main class="canvas">

  <svg width="0" height="0" style="position:absolute" aria-hidden="true">
    <defs>
      <linearGradient id="glass" x1="0" x2="1" y1="0" y2="0">
        <stop offset="0" stop-color="#c4c5c8"/>
        <stop offset="0.3" stop-color="#f3f3f4"/>
        <stop offset="0.6" stop-color="#e8e8e9"/>
        <stop offset="1" stop-color="#c6c7c9"/>
      </linearGradient>
      <linearGradient id="reflection" x1="0" x2="0" y1="0" y2="1">
        <stop offset="0" stop-color="#d6d7d9" stop-opacity="0.55"/>
        <stop offset="1" stop-color="#ffffff" stop-opacity="0"/>
      </linearGradient>
      <symbol id="bottle-body" viewBox="0 0 200 780">
        <path d="M63 40 L137 40 L137 172 C137 228 196 232 196 292 L196 694 Q196 710 181 710 L19 710 Q4 710 4 694 L4 292 C4 232 63 228 63 172 Z" fill="url(#glass)"/>
        <path d="M19 712 L181 712 Q196 712 196 726 L196 772 L4 772 L4 726 Q4 712 19 712 Z" fill="url(#reflection)"/>
        <rect x="62" y="0" width="76" height="44" rx="8" fill="#111"/>
      </symbol>
    </defs>
  </svg>

  <article class="bottle bottle--faluntera">
    <svg class="bottle__shape" viewBox="0 0 200 780" aria-hidden="true"><use href="#bottle-body"/></svg>
    <div class="neck-band"><span class="neck-band__text">OPEN&amp;SERVE</span></div>
    <div class="flavour-splash" role="img" aria-label="Scattered green splash graphic of mint, chili, lime and cucumber tones"></div>
    <h2 class="flavour-name">falu<span class="flavour-name__accent">nte</span>ra</h2>
    <p class="ingredients">fresh mint leaves,<br>green chili, lime, cucumber<br>green chili, lime, cucumber</p>
    <div class="brand"><span class="brand__mark"></span><span class="brand__name">Tovelin Spirits</span></div>
    <span class="spec spec--abv">12% alc/vol</span>
    <span class="spec spec--volume">750 ml</span>
  </article>

  <article class="bottle bottle--borvelle">
    <svg class="bottle__shape" viewBox="0 0 200 780" aria-hidden="true"><use href="#bottle-body"/></svg>
    <div class="neck-band"><span class="neck-band__text">OPEN&amp;SERVE</span></div>
    <div class="flavour-splash" role="img" aria-label="Scattered brown splash graphic of chai spice tones"></div>
    <h2 class="flavour-name">bor<span class="flavour-name__accent">vel</span>le</h2>
    <p class="ingredients">cloves, cardamom pods,<br>nutmeg, black peppercorns,<br>star anise, and cinnamon stick</p>
    <div class="brand"><span class="brand__mark"></span><span class="brand__name">Tovelin Spirits</span></div>
    <span class="spec spec--abv">12% alc/vol</span>
    <span class="spec spec--volume">750 ml</span>
  </article>

  <article class="bottle bottle--pomadrine">
    <svg class="bottle__shape" viewBox="0 0 200 780" aria-hidden="true"><use href="#bottle-body"/></svg>
    <div class="neck-band"><span class="neck-band__text">OPEN&amp;SERVE</span></div>
    <div class="flavour-splash" role="img" aria-label="Scattered pink splash graphic of lychee tones"></div>
    <h2 class="flavour-name">poma<span class="flavour-name__accent">dri</span>ne</h2>
    <p class="ingredients">cloves, cardamom pods,<br>nutmeg, black peppercorns,<br>star anise, and cinnamon stick</p>
    <div class="brand"><span class="brand__mark"></span><span class="brand__name">Tovelin Spirits</span></div>
    <span class="spec spec--abv">12% alc/vol</span>
    <span class="spec spec--volume">750 ml</span>
  </article>

</main>
</body>
</html>
```